RK LAW
Stationary Envelopes and Cards
RK LAW - Law
Creative Brief
Professional
Howard P. Lindqvist
Attorney At Law
347 N. 4th Avenue Las Vegas NV 89104
nvrklaw@mailbrook.net
NVRKLAW.NET

```html
<!DOCTYPE html>
<html lang="en">
<head>
<meta charset="utf-8">
<title>RK LAW – Stationery Set</title>
<link href="https://fonts.googleapis.com/css2?family=Open+Sans:wght@400;600;700&display=swap" rel="stylesheet">
<style>
:root{
  --bg:#f3f4f6;
  --paper:#ffffff;
  --blue:#1f5ea8;
  --blue-light:#4aa3df;
  --navy:#1b3a6b;
  --gold:#e2a623;
  --text:#4a4f57;
  --rule:#b9c3cf;
  --ink:#7a5aa6;
}
*{margin:0;padding:0;box-sizing:border-box}
html,body{width:1200px;height:552px;overflow:hidden;background:var(--bg)}
body{position:relative;font-family:"Open Sans",Arial,sans-serif;color:var(--text)}
.sheet{position:absolute;background:var(--paper);box-shadow:0 1px 4px rgba(0,0,0,.18);overflow:hidden}
.fax-sheet{left:19px;top:12px;width:360px;height:533px}
.letter-sheet{left:396px;top:12px;width:367px;height:533px}

.brand{display:flex;flex-direction:column;align-items:center}
.brand-name{font-family:"Open Sans",Arial,sans-serif;font-weight:700;font-size:20px;line-height:1;letter-spacing:1px;color:var(--blue)}
.brand-tag{font-family:"Open Sans",Arial,sans-serif;font-weight:600;font-size:5.5px;letter-spacing:1.5px;margin-top:4px;color:var(--navy)}
.sheet .brand{position:absolute;top:22px;left:0;right:0}

.fax-label{position:absolute;top:56px;right:16px;font-size:8px;font-weight:600;color:var(--navy)}
.fax-table{position:absolute;top:66px;left:16px;right:16px;border-collapse:collapse;font-size:6px}
.fax-table td{border:0.6px solid var(--rule);height:12px;padding:0 4px;color:var(--navy)}
.fax-table td.label{width:38px}
.fax-checks{position:absolute;top:143px;left:16px;right:16px;display:flex;justify-content:space-between;font-size:5.5px;color:var(--navy)}
.fax-checks span::before{content:"";display:inline-block;width:5px;height:5px;border:0.6px solid var(--navy);margin-right:3px;vertical-align:-1px}

.body-copy{position:absolute;left:16px;right:16px;font-size:5.6px;line-height:8px;text-align:justify}
.body-copy p{margin-bottom:6px}
.fax-sheet .body-copy{top:160px}
.letter-sheet .body-copy{top:92px;left:18px;right:18px}
.signature{width:54px;height:20px;border-radius:50%;background:radial-gradient(ellipse,rgba(122,90,166,.45),rgba(122,90,166,0) 70%);margin:4px 0 2px}
.signer{color:var(--navy)}

.footer-bands{position:absolute;left:0;bottom:0;width:100%;display:flex;flex-direction:column}
.band-gold{height:4px;background:var(--gold)}
.band-light{height:4px;background:var(--blue-light)}
.band-main{height:34px;background:var(--blue)}
.footer-contact{position:absolute;right:14px;bottom:6px;text-align:right;color:#fff;font-size:5.4px;line-height:7.5px}

.card{position:absolute;width:191px;height:110px;box-shadow:0 1px 4px rgba(0,0,0,.18);overflow:hidden}
.card-front{left:800px;top:29px;background:var(--paper)}
.card-back{left:1000px;top:29px;background:linear-gradient(135deg,var(--blue-light),var(--blue))}
.card-front .brand{position:absolute;top:16px;left:12px;align-items:flex-start}
.card-front .brand-name{font-size:14px}
.card-front .brand-tag{font-size:4px;margin-top:3px}
.card-person{position:absolute;top:14px;right:12px;text-align:right;color:var(--navy)}
.card-person .name{font-size:7.5px;font-weight:600}
.card-person .title{font-size:5.5px}
.card-front .band-gold,.card-front .band-light{height:3px}
.card-front .band-main{height:28px}
.card-front .footer-contact{font-size:4.8px;line-height:6.5px;right:10px;bottom:4px}
.card-back .brand{position:absolute;inset:0;justify-content:center}
.card-back .brand-name{color:#fff}
.card-back .brand-tag{color:#fff}

.envelope{position:absolute;left:800px;top:216px;width:386px;height:288px;background:var(--paper);box-shadow:0 1px 4px rgba(0,0,0,.18);overflow:hidden}
.envelope .brand{position:absolute;top:18px;left:16px;align-items:flex-start}
.envelope .brand-name{font-size:16px}
.envelope .brand-tag{font-size:4.5px}
.envelope .band-main{height:40px}
</style>
</head>
<body>

<section class="sheet fax-sheet">
  <div class="brand"><div class="brand-name">RK LAW</div><div class="brand-tag">ATTORNEY AT LAW</div></div>
  <div class="fax-label">FAX</div>
  <table class="fax-table">
    <tr><td class="label">To:</td><td></td><td class="label">From:</td><td></td></tr>
    <tr><td class="label">Fax:</td><td></td><td class="label">Pages:</td><td></td></tr>
    <tr><td class="label">Phone:</td><td></td><td class="label">Date:</td><td></td></tr>
    <tr><td class="label">Re:</td><td></td><td class="label">CC:</td><td></td></tr>
    <tr><td class="label"></td><td></td><td class="label"></td><td></td></tr>
  </table>
  <div class="fax-checks"><span>Urgent</span><span>For Review</span><span>Please Comment</span><span>Please Reply</span><span>Please Recycle</span></div>
  <div class="body-copy">
    <p>Thank you for meeting with our office this week. We have reviewed the documents you provided and prepared a summary of the key points in your matter. Our team will contact the other party and request the records needed to move forward. Please keep copies of all letters you receive and forward them to us as soon as possible so that we can respond within the required time.</p>
    <p>At this stage we recommend that you avoid discussing the case with anyone other than your attorney. Any statement made now may be used later, so it is best to direct all questions to our office.</p>
    <p>We will send a full update once the hearing date is set. If you have any questions in the meantime, please call or write to us and we will be glad to help.</p>
    <p>Yours Sincerely,</p>
    <div class="signature" role="img" aria-label="Handwritten signature"></div>
    <p class="signer">Howard P. Lindqvist</p>
  </div>
  <div class="footer-bands"><div class="band-gold"></div><div class="band-light"></div><div class="band-main"></div></div>
  <div class="footer-contact">347 N. 4th Avenue Las Vegas NV 89104<br>(702) 555-0148 · plumvex<br>nvrklaw@mailbrook.net · NVRKLAW.NET</div>
</section>

<section class="sheet letter-sheet">
  <div class="brand"><div class="brand-name">RK LAW</div><div class="brand-tag">ATTORNEY AT LAW</div></div>
  <div class="body-copy">
    <p>Jordan Ellison<br>100 Harbor Street<br>Brisbane, Australia</p>
    <p>Dear Jordan Ellison,</p>
    <p>Thank you for meeting with our office this week. We have reviewed the documents you provided and prepared a summary of the key points in your matter. Our team will contact the other party and request the records needed to move forward. Please keep copies of all letters you receive and forward them to us as soon as possible so that we can respond within the required time.</p>
    <p>At this stage we recommend that you avoid discussing the case with anyone other than your attorney. Any statement made now may be used later, so it is best to direct all questions to our office.</p>
    <p>We will send a full update once the hearing date is set. If you have any questions in the meantime, please call or write to us and we will be glad to help.</p>
    <p>Thank you for meeting with our office this week. We have reviewed the documents you provided and prepared a summary of the key points in your matter. Our team will contact the other party and request the records needed to move forward. Please keep copies of all letters you receive and forward them to us as soon as possible so that we can respond within the required time.</p>
    <p>Yours Sincerely,</p>
    <div class="signature" role="img" aria-label="Handwritten signature"></div>
    <p class="signer">Howard P. Lindqvist</p>
  </div>
  <div class="footer-bands"><div class="band-gold"></div><div class="band-light"></div><div class="band-main"></div></div>
  <div class="footer-contact">347 N. 4th Avenue Las Vegas NV 89104<br>(702) 555-0148 · plumvex<br>nvrklaw@mailbrook.net · NVRKLAW.NET</div>
</section>

<section class="card card-front">
  <div class="brand"><div class="brand-name">RK LAW</div><div class="brand-tag">ATTORNEY AT LAW</div></div>
  <div class="card-person"><div class="name">Howard P. Lindqvist</div><div class="title">Attorney At Law</div></div>
  <div class="footer-bands"><div class="band-gold"></div><div class="band-main"></div></div>
  <div class="footer-contact">347 N. 4th Avenue Las Vegas NV 89104<br>(702) 555-0148 · nvrklaw@mailbrook.net<br>NVRKLAW.NET</div>
</section>

<section class="card card-back">
  <div class="brand"><div class="brand-name">RK LAW</div><div class="brand-tag">ATTORNEY AT LAW</div></div>
</section>

<section class="envelope">
  <div class="brand"><div class="brand-name">RK LAW</div><div class="brand-tag">ATTORNEY AT LAW</div></div>
  <div class="footer-bands"><div class="band-gold"></div><div class="band-light"></div><div class="band-main"></div></div>
  <div class="footer-contact">347 N. 4th Avenue Las Vegas NV 89104<br>(702) 555-0148 · plumvex<br>nvrklaw@mailbrook.net · NVRKLAW.NET</div>
</section>

</body>
</html>
```